Modern Lawfirm Business Card Design

We're looking for a business card to incorporate the newly created logo we had made.

Ideally looking for a law firm business card demonstrating, modern, minimalist, strong/bold design.

I'm open to any design honestly, but nothing "flashy".

Target Market(s)

Immigration law, family immigration, humanitarian, general legal

Industry/Entity Type

Law Firm

Contact Information for Business Card

Please use dummy information, name, street address, city, state, phone number, email, website.

Font styles to use
Serif
Sans Serif

Requirements
Must have
• Please use dummy information, name, street address, city, state, phone number, email, website.

```html
<!DOCTYPE html>
<html lang="en">
<head>
<meta charset="utf-8">
<title>Andres Villalta – Business Card</title>
<link rel="stylesheet" href="https://fonts.googleapis.com/css2?family=Oswald:wght@300;400&display=swap">
<style>
  :root {
    --backdrop: #e4e5e8;
    --card: #ffffff;
    --ink: #245c9c;
    --rule: #3c62aa;
    --band: #1b62a1;
    --band-text: #ffffff;
  }
  * { box-sizing: border-box; margin: 0; padding: 0; }
  html, body {
    width: 1200px; height: 1200px; overflow: hidden;
    background: var(--backdrop);
  }
  .business-card {
    position: absolute;
    left: 145px; top: 340px;
    width: 911px; height: 519px;
    background: var(--card);
    font-family: "Oswald", sans-serif;
    font-weight: 300;
    color: var(--ink);
  }
  .holder-name {
    position: absolute;
    left: 0; right: 0; top: 52px;
    text-align: center;
    font-weight: 400;
    font-size: 56px;
    letter-spacing: 2px;
    line-height: 1;
  }
  .contact-table {
    position: absolute;
    left: 103px; top: 154px;
    width: 703px;
    border-top: 1px solid var(--rule);
  }
  .contact-row {
    display: flex;
    height: 52px;
    border-bottom: 1px solid var(--rule);
  }
  .contact-cell {
    display: flex;
    align-items: center;
    justify-content: center;
    font-size: 22px;
    letter-spacing: 0.4px;
    white-space: nowrap;
  }
  .contact-cell + .contact-cell { border-left: 1px solid var(--rule); }
  .brand-band {
    position: absolute;
    left: 52px; top: 413px;
    width: 806px; height: 52px;
    background: var(--band);
    display: flex;
    align-items: center;
    justify-content: center;
  }
  .brand-name {
    color: var(--band-text);
    font-weight: 400;
    font-size: 19px;
    letter-spacing: 2px;
  }
</style>
</head>
<body>
  <main class="business-card">
    <h1 class="holder-name">ANDRES VILLALTA</h1>

    <section class="contact-table">
      <div class="contact-row">
        <div class="contact-cell" style="width:52px">Ad</div>
        <div class="contact-cell" style="width:260px">418 Calloway Ave, 12st</div>
        <div class="contact-cell" style="width:156px">Maple Blv</div>
        <div class="contact-cell" style="flex:1">Veran, HN 00712</div>
      </div>
      <div class="contact-row">
        <div class="contact-cell" style="width:209px">Phone</div>
        <div class="contact-cell" style="flex:1">555-0142786</div>
      </div>
      <div class="contact-row">
        <div class="contact-cell" style="width:157px">Mail</div>
        <div class="contact-cell" style="flex:1">andres@villalta.com</div>
      </div>
      <div class="contact-row">
        <div class="contact-cell" style="width:209px">Website</div>
        <div class="contact-cell" style="flex:1">www.andresvillalta.com</div>
      </div>
    </section>

    <footer class="brand-band">
      <span class="brand-name">HALVERN</span>
    </footer>
  </main>
</body>
</html>
```